Innovative mission-driven diversity services company needs launch brochure

Two-sided 8 1/5" x 11" document to demonstrate a new program.

Target Market(s)

Chief Diversity Officers and Hiring Managers at advertising/communications agencies who are looking to attract and hire recently graduated/about to graduate African American students

Industry/Entity Type

It Company

Requirements
Must have
• a very contemporary feel that will well represent the vibrancy, energy, and identity of the African American student population. This is a cause driven organization and that passion and purpose should be conveyed while recognizing that the target audience are corporate executives.

```html
<!DOCTYPE html>
<html lang="en">
<head>
<meta charset="utf-8">
<title>Keystone LLC – Launch Brochure</title>
<link href="https://fonts.googleapis.com/css2?family=Oswald:wght@500;600&family=Libre+Baskerville:wght@700&family=Montserrat:wght@700&family=Roboto:wght@400;500;700&family=Playfair+Display:ital@1&display=swap" rel="stylesheet">
<style>
:root{
  --blue:#1467b3;
  --red:#c8102e;
  --dark-red:#a50e26;
  --ink:#222;
  --muted:#555;
  --rule:#9a9a9a;
  --bg:#e6e1d9;
  --card-line:#e2e2e2;
}
*{box-sizing:border-box;margin:0;padding:0}
html,body{width:1200px;height:944px;overflow:hidden;background:var(--bg);font-family:Roboto,Arial,sans-serif;color:var(--ink)}
.page{position:absolute;top:118px;width:520px;height:736px;background:#fff;box-shadow:0 4px 14px rgba(0,0,0,.25);overflow:hidden}
.page--front{left:50px}
.page--back{left:619px}
.abs{position:absolute}

/* front */
.brand-name{left:24px;top:20px;font-family:"Libre Baskerville",serif;font-weight:700;font-size:48px;color:var(--blue);line-height:1}
.front-title{left:24px;top:78px;font-family:Oswald,sans-serif;font-weight:500;font-size:25px;color:#222;letter-spacing:-.2px}
.front-tagline{left:24px;top:114px;font-size:9.5px;font-weight:700;color:var(--red);width:330px;line-height:1.25}
.rule{height:1px;background:var(--rule)}
.intro{left:40px;top:152px;width:440px;text-align:center;font-size:10.5px;line-height:1.3;color:#333}
.chart-title{left:0;top:197px;width:520px;text-align:center;font-family:Montserrat,sans-serif;font-size:11px;color:var(--blue);letter-spacing:.2px}
.chart-year{top:222px;font-size:13px;color:#333;font-weight:500}
.bar{background:linear-gradient(90deg,var(--dark-red) 0 50%,var(--red) 50%);width:58px;bottom:405px;display:flex;align-items:flex-end;justify-content:center;padding-bottom:6px;font-family:Oswald,sans-serif;font-size:17px;color:#fff}
.bar-label{top:339px;width:100px;text-align:center;font-size:7.5px;line-height:1.35;color:#444;letter-spacing:.3px}
.chart-base{left:48px;top:331px;width:430px;height:1px;background:#ccc}
.note{left:20px;top:376px;width:485px;font-size:8.6px;line-height:1.3;color:#333}
.note p+p{margin-top:3px}
.band{height:30px;display:flex;align-items:center;justify-content:center;font-family:Oswald,sans-serif;font-weight:500;font-size:13.5px;color:#fff;letter-spacing:-.2px}
.band--blue{background:var(--blue)}
.band--red{background:var(--red)}
.news-card{border:1px solid #ccc;background:#fff;overflow:hidden}
.news-card__kicker{font-size:5px;color:#888;font-weight:700;letter-spacing:.5px}
.news-card__headline{font-family:Roboto,sans-serif;font-weight:700;font-size:12px;line-height:1.1;color:#222;margin-top:3px;letter-spacing:-.2px}
.share-row{display:flex;gap:3px;margin-top:5px}
.share-row span{width:20px;height:7px;display:block}
.news-card__byline{font-size:4.5px;color:#888;margin-top:4px}
.portrait{width:64px;height:64px;border-radius:50%;background:radial-gradient(circle at 50% 40%,#b38d74,#4d3a30);left:8px;top:13px}
.quote{left:84px;top:8px;width:166px;max-width:166px;white-space:normal;font-family:"Playfair Display",serif;font-style:italic;font-size:8px;line-height:1.4;color:#222}
.quote-name{left:84px;top:66px;font-size:8.5px;font-weight:700}
.quote-role{left:84px;top:78px;font-size:6.5px;font-weight:700;white-space:nowrap}
.quote-mark{left:228px;top:56px;font-family:Oswald,sans-serif;font-size:50px;color:#eee;line-height:1}
.photo{height:55px}
.caption{font-size:8.5px;line-height:1.35;color:#555;width:145px}

/* back */
.mission-title{left:16px;top:30px;font-family:"Libre Baskerville",serif;font-weight:700;font-size:28px;line-height:1.15}
.mission-title .red{color:var(--red)}
.mission-title .blue{color:var(--blue)}
.mission-statement{left:290px;top:38px;width:215px;font-size:9.6px;font-weight:700;line-height:1.4;color:#111}
.step{background:#fff;border:1px solid var(--card-line);border-radius:4px;box-shadow:0 1px 3px rgba(0,0,0,.06);padding:10px 9px}
.step h3{font-family:Montserrat,sans-serif;font-size:11px;color:var(--blue);line-height:1.15}
.step p{font-size:7.9px;line-height:1.35;color:#333;margin-top:12px}
.step--split{display:flex;gap:12px}
.about-band{left:26px;top:493px;width:468px;height:35px;background:var(--blue);color:#fff;font-family:"Libre Baskerville",serif;font-weight:700;font-size:18px;display:flex;align-items:center;padding-left:22px}
.about-copy{left:33px;top:546px;width:460px;font-size:8.6px;line-height:1.5;color:#333}
.about-copy p+p{margin-top:12px}
</style>
</head>
<body>

<section class="page page--front">
  <div class="abs brand-name">Keystone LLC</div>
  <h1 class="abs front-title">Narrowing the Racial Diversity Gap</h1>
  <p class="abs front-tagline">A powerful new approach to increasing the African-American employment rate in the communications industry</p>

  <div class="abs rule" style="left:25px;top:144px;width:470px"></div>
  <p class="abs intro">Despite efforts to increase participation, African-American rates of employment in the communications industry have actually declined over the past decade</p>
  <div class="abs rule" style="left:25px;top:189px;width:470px"></div>

  <h2 class="abs chart-title">AFRICAN-AMERICAN PROPORTION OF WORKFORCE*</h2>
  <div class="abs chart-year" style="left:126px">2015</div>
  <div class="abs chart-year" style="left:340px">2016</div>
  <div class="abs chart-base"></div>
  <div class="abs bar" style="left:60px;height:81px">11%</div>
  <div class="abs bar" style="left:150px;height:50px">7%</div>
  <div class="abs bar" style="left:274px;height:91px">12%</div>
  <div class="abs bar" style="left:363px;height:36px">5%</div>
  <div class="abs bar-label" style="left:39px">OVERALL<br>WORKFORCE</div>
  <div class="abs bar-label" style="left:129px">COMMUNICATIONS<br>INDUSTRY</div>
  <div class="abs bar-label" style="left:253px">OVERALL<br>WORKFORCE</div>
  <div class="abs bar-label" style="left:342px">COMMUNICATIONS<br>INDUSTRY</div>

  <div class="abs note">
    <p>While the communications agency hiring rate of people of Hispanic or Asian origin has reached parity with their overall work-force participation rates, African-American participation has actually dropped by nearly a third.</p>
    <p>Communications agencies have identified this gap as a critical issue but are falling further behind on AA hiring.<br>*REFERENCE TO COME</p>
  </div>

  <div class="abs band band--blue" style="left:21px;top:434px;width:478px">CLIENTS HAVE NOW BEGUN TO DIRECTLY EXERT PRESSURE ON THE INDUSTRY</div>

  <article class="abs news-card" style="left:23px;top:478px;width:183px;height:92px;padding:6px 11px">
    <div class="news-card__kicker">BRANDS</div>
    <div class="news-card__headline">Harvest Grain Foods Insists Future Agencies Meet Specific Diversity Quotas</div>
    <div class="share-row"><span style="background:#3b5998"></span><span style="background:#55acee"></span><span style="background:#e04a3a"></span></div>
    <div class="news-card__byline">By Staff Writer on Aug 31, 2016</div>
  </article>

  <article class="abs news-card" style="left:238px;top:478px;width:261px;height:92px">
    <div class="abs portrait" role="img" aria-label="Portrait photo of the quoted agency association executive"></div>
    <div class="abs quote-mark">”</div>
    <div class="abs quote">“In order to push yourself to have a more diverse work force you have to be intentional about it — and nothing will drive intent faster than a client’s dollar”</div>
    <div class="abs quote-name">Dana Whitfield</div>
    <div class="abs quote-role">President &amp; CEO, Agency Alliance</div>
  </article>

  <div class="abs band band--red" style="left:21px;top:581px;width:478px">WHY ARE COMMUNICATIONS AGENCIES FAILING TO INCREASE THE AA HIRING RATE?</div>

  <div class="abs photo" style="left:21px;top:626px;width:131px;background:linear-gradient(135deg,#a84a4a,#4a4a58 60%,#2a2a30)" role="img" aria-label="Photo of an industry panel discussion on stage"></div>
  <div class="abs photo" style="left:189px;top:626px;width:131px;background:linear-gradient(90deg,#e6c9a0,#d9534f 50%,#f1e6d2)" role="img" aria-label="Illustration of faces in profile with striped pattern"></div>
  <div class="abs photo" style="left:355px;top:626px;width:131px;background:linear-gradient(180deg,#f2f2f2,#d8d8d8 60%,#2c2c2c)" role="img" aria-label="Photo of a graduate in cap holding a sign"></div>
  <p class="abs caption" style="left:21px;top:686px">An industry too inwardly focused to realize that it can be offputting</p>
  <p class="abs caption" style="left:189px;top:686px">Assuming barriers to hiring all people of color are the same and are not unique to each group</p>
  <p class="abs caption" style="left:355px;top:686px">Dramatic disconnection from the most critical candidate pool that can provide an immediate &amp; lasting impact</p>
</section>

<section class="page page--back">
  <h1 class="abs mission-title"><span class="red">The</span> <span class="blue">Keystone</span><br><span class="red">Mission</span></h1>
  <p class="abs mission-statement">Drive parity in opportunity and representation for the most promising young African-American minds while creating a cultural and competitive advantage for progressive communications organizations</p>
  <div class="abs rule" style="left:22px;top:126px;width:471px"></div>

  <svg class="abs" style="left:0;top:0" width="520" height="400" viewBox="0 0 520 400" aria-hidden="true">
    <g fill="none" stroke="#c8102e" stroke-width="2">
      <path d="M26 147 H478 Q490 147 490 159 V338 Q490 350 478 350 H38 Q26 350 26 362 V363 Q26 375 38 375 H493"/>
      <path d="M129 142 L134 147 L129 152 M281 142 L286 147 L281 152 M486 263 L490 269 L494 263 M407 345 L402 350 L407 355 M100 345 L95 350 L100 355 M239 370 L244 375 L239 380" stroke-width="1.5"/>
    </g>
    <g fill="#c8102e">
      <circle cx="78" cy="147" r="5"/><circle cx="192" cy="147" r="5"/><circle cx="368" cy="147" r="5"/>
      <circle cx="129" cy="375" r="5"/><circle cx="374" cy="375" r="5"/>
    </g>
  </svg>

  <div class="abs step" style="left:26px;top:160px;width:105px;height:134px">
    <h3>Community Connection</h3>
    <p>Keystone works closely with the African-American communities within relevant college programs with a strong focus on HBCUs</p>
  </div>
  <div class="abs step" style="left:142px;top:160px;width:107px;height:149px">
    <h3>Identification &amp; Vetting</h3>
    <p>Candidates are identified through community connection and formally assessed for relevant agency technology skills, emotional, cultural and academic prowess.</p>
  </div>
  <div class="abs step" style="left:263px;top:160px;width:212px;height:176px">
    <h3 style="margin-top:6px">Multi-Focal Training</h3>
    <div class="step--split">
      <p style="width:66px">Training program specific to advertising industry, to include all major disciplines.</p>
      <p style="flex:1">Coaching provided to crystallize candidate’s personal brand and voice, to improve the communication of value and reduce time spent ‘trying to figure out.’ Coaching also focuses on personal presentation and professional etiquette training to facilitate corporate integration.</p>
    </div>
  </div>
  <div class="abs step" style="left:26px;top:389px;width:203px;height:86px">
    <h3>Onboarding Support</h3>
    <p style="margin-top:9px">New hires will be provided innovative e-development platform with personal mentor, to ensure successful onboarding.</p>
  </div>
  <div class="abs step" style="left:245px;top:389px;width:248px;height:86px">
    <h3>Community Building</h3>
    <p style="margin-top:9px">Each Keystone candidate signs an agreement to initiate a mentoring relationship with a young African American professional hired after them within their organization.</p>
  </div>

  <h2 class="abs about-band">About Keystone LLC</h2>
  <div class="abs about-copy">
    <p>Keystone is a B Corp (for-profit social enterprise) created by two principles with direct and complimentary experiences in tackling related challenges.</p>
    <p>Maya Brooks has created a highly successful coaching practice focused on helping soon to graduate, or recently graduated, college students find purpose-driven careers. She is also the founder and Executive Director of the Bridgeway Foundation which provides guidance and assistance for young adults who are “aging out” of the welfare system with over half of the foundation’s fellows being African-American.</p>
    <p>Grant Ellison spent his career in the advertising business culminating in running leading agencies at both Northstar Group and Meridian Holdings. He has personally dealt with the barriers and frustrations in identifying and attracting talent from the African-American business community despite significant corporate efforts. He has also witnessed the significant advantages gained when truly diversified teams are assembled and nurtured.</p>
  </div>
</section>

</body>
</html>
```